"Tidewell Fellowship" needs a logo design that represents a Christian family boating ministry

Mission Statement:
“Providing compassion, care and opportunities to create memories for marginalized groups of society through ocean therapy.”
Bible verse:
Colossians 3:12 – “Therefore, as God’s chosen people, holy and dearly loved, clothe yourselves with compassion, kindness, humility, gentleness and patience.”
Target Market(s)
HOMELESS (who have gone through shelters and are on the road to recovery)
CHURCH GROUPS
INJURED MILITARY VETERANS
YOUTH AT RISK (orphans, human trafficking survivors)
SICKLY (hospitalized who can get out once in a while)
CAREGIVERS (single moms, military spouses caring for injured vets, families of those in prison)
ELDERLY (retirement centers)
SMALL BUSINESS STAFF OUTINGS
SPECIAL EVENTS
Industry/Entity Type
Ministry
Contact Information for Business Card
Captain Glen Marlowe @ 808-491-3027
Priscilla Marlowe @ 808-493-5184
info@tidewellfellowship.example
www.tidewellfellowship.example (not active yet but hopefully, soon)
Requirements
Must have
- Catch-phrase words maybe for back of business card:
- "Tide-Bound --- Kindness --- Making moments out at sea"
Nice to have
- Added 2 photo files just for visuals:
- 1 photo is of our boat.
- Other photo is our daughter's artwork on a cooler she made (for father's day gift)...might be nice and fun to incorporate daughter's artwork/inspiration into logo...but not sure if it looks to busy

```html
<!DOCTYPE html>
<html lang="en">
<head>
<meta charset="utf-8">
<title>Tidewell Fellowship – Business Cards</title>
<link rel="stylesheet" href="https://fonts.googleapis.com/css2?family=Orbitron:wght@500;700&display=swap">
<style>
  :root {
    --page-bg: #ecedef;
    --navy: #1f2535;
    --navy-soft: #2c3345;
    --ink-light: #f1f2f4;
    --chip-grey: #d9dbdf;
    --tan-dark: #5a4636;
    --tan: #b88c68;
    --tan-light: #e3cdb6;
    --sea-grey: #8d98a8;
    --sea-light: #cfd5dd;
    --sea-blue: #5fb4c9;
  }
  * { box-sizing: border-box; margin: 0; padding: 0; }
  html, body { width: 1200px; height: 1000px; overflow: hidden; }
  body {
    background: var(--page-bg);
    font-family: "Orbitron", "Arial Narrow", sans-serif;
    display: flex;
    align-items: center;
    justify-content: center;
    gap: 40px;
  }
  .card {
    position: relative;
    width: 540px;
    height: 310px;
    overflow: hidden;
    box-shadow: 0 10px 28px rgba(20, 25, 40, 0.25);
  }
  .card-art { position: absolute; inset: 0; width: 100%; height: 100%; }
  .photo-hands {
    position: absolute; inset: 0;
    background: linear-gradient(100deg, var(--tan-dark) 0%, var(--tan) 40%, var(--tan-light) 70%, #c9b29c 100%);
  }
  .photo-boat {
    position: absolute; inset: 0;
    background: linear-gradient(160deg, var(--sea-light) 0%, var(--sea-grey) 55%, #aab3bf 100%);
  }
  .holder-names {
    position: absolute; top: 20px; left: 152px;
    color: var(--navy); font-weight: 700; font-size: 21px;
    letter-spacing: 1px; line-height: 1.25; text-transform: uppercase;
    white-space: nowrap;
  }
  .holder-names .amp { display: block; padding-left: 56px; }
  .contact-panel {
    position: absolute; top: 100px; left: 22px; width: 220px;
    color: var(--ink-light); font-size: 9.5px; font-weight: 500; line-height: 1.5;
  }
  .contact-row { display: flex; align-items: flex-start; gap: 8px; margin-bottom: 8px; white-space: nowrap; }
  .contact-row svg { flex: none; width: 14px; height: 14px; margin-top: 1px; }
  .surname {
    position: absolute; top: 168px; left: 300px; width: 220px; height: 40px;
    display: flex; align-items: center; justify-content: center;
    background: var(--chip-grey);
    color: var(--navy); font-weight: 700; font-size: 20px; letter-spacing: 1px;
  }
  .brand-mark {
    position: absolute; top: 62px; right: 20px; height: 38px;
    display: flex; align-items: center; gap: 10px;
    padding: 0 14px;
    background: var(--chip-grey);
    white-space: nowrap;
  }
  .brand-dot { flex: none; width: 16px; height: 16px; border-radius: 50%; background: var(--sea-blue); }
  .brand-name {
    color: var(--navy); font-weight: 700; font-size: 15px; letter-spacing: 0.5px; text-transform: uppercase;
  }
  .catchphrase {
    position: absolute; top: 140px; left: 150px;
    color: var(--ink-light); font-size: 12px; font-weight: 500;
    line-height: 1.9; letter-spacing: 0.8px; text-transform: uppercase;
    list-style: none; white-space: nowrap;
  }
</style>
</head>
<body>

  <section class="card card-front">
    <div class="photo-hands" role="img" aria-label="Soft-focus photograph of joined hands in warm tones"></div>
    <svg class="card-art" viewBox="0 0 540 310" aria-hidden="true">
      <polygon points="0,0 140,0 140,80 0,80" fill="var(--navy)"/>
      <polygon points="0,80 250,80 250,200 0,220" fill="var(--navy)" opacity="0.92"/>
      <polygon points="0,220 250,200 300,310 0,310" fill="var(--navy-soft)"/>
      <polygon points="460,0 540,0 540,50 485,50" fill="var(--navy)"/>
    </svg>
    <h1 class="holder-names">Captain Glen<span class="amp">&amp; Priscilla</span></h1>
    <div class="contact-panel">
      <div class="contact-row">
        <svg viewBox="0 0 24 24"><path fill="var(--ink-light)" d="M6.6 10.8a15 15 0 0 0 6.6 6.6l2.2-2.2c.3-.3.7-.4 1-.2 1.1.4 2.3.6 3.6.6.6 0 1 .4 1 1V20c0 .6-.4 1-1 1A17 17 0 0 1 3 4c0-.6.4-1 1-1h3.5c.6 0 1 .4 1 1 0 1.3.2 2.5.6 3.6.1.3 0 .7-.2 1z"/></svg>
        <div>808-493-5184<br>808-491-3027</div>
      </div>
      <div class="contact-row">
        <svg viewBox="0 0 24 24"><circle cx="12" cy="12" r="9" fill="none" stroke="var(--ink-light)" stroke-width="2"/><path d="M3 12h18M12 3c3 3.5 3 14.5 0 18M12 3c-3 3.5-3 14.5 0 18" fill="none" stroke="var(--ink-light)" stroke-width="1.6"/></svg>
        <div>www.tidewellfellowship.example</div>
      </div>
      <div class="contact-row">
        <svg viewBox="0 0 24 24"><path fill="var(--ink-light)" d="M12 2a7 7 0 0 0-7 7c0 5 7 13 7 13s7-8 7-13a7 7 0 0 0-7-7zm0 9.5A2.5 2.5 0 1 1 12 6.5a2.5 2.5 0 0 1 0 5z"/></svg>
        <div>info@tidewellfellowship.example</div>
      </div>
    </div>
    <p class="surname">MARLOWE</p>
  </section>

  <section class="card card-back">
    <div class="photo-boat" role="img" aria-label="Soft-focus photograph of a boat at the marina"></div>
    <svg class="card-art" viewBox="0 0 540 310" aria-hidden="true">
      <polygon points="0,0 60,0 0,70" fill="var(--navy)"/>
      <polygon points="130,110 470,110 470,250 130,250" fill="var(--navy)" opacity="0.94"/>
      <polygon points="0,260 540,250 540,310 0,310" fill="var(--navy)"/>
      <polygon points="480,110 540,110 540,250 480,250" fill="var(--navy-soft)"/>
    </svg>
    <div class="brand-mark">
      <span class="brand-dot"></span>
      <span class="brand-name">Tidewell Fellowship</span>
    </div>
    <ul class="catchphrase">
      <li>Tide-Bound</li>
      <li>Kindness</li>
      <li>Making moments out at sea</li>
    </ul>
  </section>

</body>
</html>
```